kashvel LED lighting Brochure design *

need a Brochure for kashvel LED, that is a company specialises in industrial LED lighting solutions ... we also do retail, gas stations as well...
we are formed to serve customer need in lighting doing engineering, supply and installation of LED lighting
we need a Brochure that describe our company work, project cycle, project reference and services provided in addition to our main products that will be provided to consultant for product range approval

Target Market(s)

industrial sector (petrochemical, chemical, factories), construction, retail shops, gas stations

Industry/Entity Type

Lighting

Colors

Designer to choose colors to be used in the design.

Requirements
Must have
• project cycle
• project reference photos... cant upload it here

```html
<!DOCTYPE html>
<html lang="en">
<head>
<meta charset="utf-8">
<title>kashvel LED lighting – Brochure</title>
<link rel="stylesheet" href="https://fonts.googleapis.com/css2?family=Montserrat:wght@400;500;600;700;800&display=swap">
<style>
:root{
  --bg:#e9eaec;
  --paper:#ffffff;
  --navy:#1b2b45;
  --teal:#2bb3c1;
  --orange:#f6a91b;
  --blue:#1f5fa6;
  --red:#e2403a;
  --green:#7cb342;
  --purple:#7b4a9c;
  --ink:#3d4452;
  --muted:#8a909b;
  --line:#d6d9de;
}
*{box-sizing:border-box;margin:0;padding:0}
html,body{width:1200px;height:2512px;overflow:hidden;background:var(--bg);font-family:"Montserrat",sans-serif;color:var(--ink)}
.sheet{position:relative;width:1200px;height:2512px}
.page{position:absolute;width:400px;height:566px;background:var(--paper);box-shadow:0 4px 14px rgba(0,0,0,.12);overflow:hidden}
.brand{position:absolute;top:22px;left:22px;display:flex;align-items:center;gap:7px;font-weight:800;font-size:15px;color:var(--navy);letter-spacing:.5px}
.brand-square{width:14px;height:14px;background:var(--orange)}
.tile{position:absolute;width:68px;height:68px;border-radius:10px}
.tile.navy{background:var(--navy)}
.tile.orange{background:var(--orange)}
.tile.teal{background:var(--teal)}
.tile.outline-teal{border:3px solid var(--teal)}
.tile.outline-red{border:3px solid var(--red)}
.tile.outline-navy{border:3px solid var(--navy)}
.photo{background:linear-gradient(135deg,#0f3a6e 0%,#1f6fb4 45%,#6fc3e6 75%,#1a4a84 100%)}
.photo-warm{background:linear-gradient(135deg,#6b4b2b,#c98b3d 50%,#e8c27a)}
.cover-title{position:absolute;top:76px;left:22px;width:230px;font-size:19px;line-height:1.2;font-weight:800;color:var(--teal);text-transform:uppercase}
.contact-list{position:absolute;top:120px;left:170px;list-style:none;font-size:10.5px;color:var(--ink)}
.contact-list li{display:flex;align-items:center;gap:8px;margin-bottom:13px}
.contact-list svg{width:14px;height:14px;fill:var(--teal)}
.label-box{position:absolute;top:0;left:22px;width:120px;height:110px;background:var(--teal);color:#fff;font-weight:700;font-size:22px;padding:60px 12px 0;line-height:1}
.body-copy{font-size:10px;line-height:1.6;color:var(--ink)}
.slogan{position:absolute;left:40px;top:452px;font-weight:700;font-size:15px;color:var(--navy)}
.slogan em{display:block;font-style:normal;color:var(--orange);font-size:12px;margin-top:4px}
.heading{position:absolute;left:22px;font-weight:800;color:var(--teal);line-height:1.05}
.ref-grid{position:absolute;top:140px;left:40px;display:grid;grid-template-columns:repeat(3,90px);gap:18px 24px}
.ref-badge{height:38px;border-radius:4px;background:#e3e6ea}
.ref-badge.round{border-radius:50%;width:38px;margin:0 auto}
.service-list{position:absolute;top:120px;left:22px;right:22px;list-style:none}
.service-list li{height:32px;margin-bottom:12px;display:flex;align-items:center;color:#fff;font-weight:600;font-size:11px;padding-left:12px;border-radius:0 16px 16px 0}
.cycle{position:absolute;left:70px;top:170px;width:260px;height:260px;border-radius:50%;
  background:conic-gradient(var(--orange) 0 45deg,var(--red) 45deg 90deg,var(--purple) 90deg 135deg,var(--blue) 135deg 180deg,var(--teal) 180deg 225deg,var(--green) 225deg 270deg,var(--navy) 270deg 315deg,#f2c94c 315deg 360deg)}
.cycle-hub{position:absolute;left:65px;top:65px;width:130px;height:130px;border-radius:50%;background:#fff;display:flex;align-items:center;justify-content:center;text-align:center;font-weight:800;font-size:14px;color:var(--navy)}
.cycle-labels{position:absolute;left:22px;right:22px;top:450px;list-style:none;display:grid;grid-template-columns:1fr 1fr;gap:6px 14px;font-size:10px}
.cycle-labels li{display:flex;align-items:center;gap:6px}
.cycle-labels i{width:10px;height:10px;display:inline-block}
</style>
</head>
<body>
<main class="sheet">

  <!-- Front cover -->
  <section class="page cover" style="left:170px;top:50px">
    <div class="brand"><span class="brand-square"></span>kashvel</div>
    <h1 class="cover-title">Engineering Lighting Solution Provider</h1>
    <div role="img" aria-label="Photo of an illuminated industrial lighting network seen from above">
      <div class="tile photo" style="left:40px;top:165px"></div>
      <div class="tile photo" style="left:114px;top:165px"></div>
      <div class="tile photo" style="left:188px;top:165px"></div>
      <div class="tile photo" style="left:262px;top:165px"></div>
      <div class="tile photo" style="left:40px;top:239px"></div>
      <div class="tile photo" style="left:114px;top:239px"></div>
      <div class="tile photo" style="left:188px;top:239px"></div>
      <div class="tile photo" style="left:262px;top:239px"></div>
      <div class="tile photo" style="left:114px;top:313px"></div>
      <div class="tile photo" style="left:188px;top:313px"></div>
    </div>
    <div class="tile orange" style="left:262px;top:91px"></div>
    <div class="tile navy" style="left:40px;top:313px"></div>
    <div class="tile outline-teal" style="left:262px;top:313px"></div>
    <div class="tile navy" style="left:40px;top:387px"></div>
    <div class="tile teal" style="left:114px;top:387px"></div>
    <div class="tile orange" style="left:188px;top:387px"></div>
    <div class="tile outline-red" style="left:114px;top:461px"></div>
  </section>

  <!-- Back cover -->
  <section class="page back-cover" style="left:630px;top:50px">
    <div class="brand"><span class="brand-square"></span>kashvel</div>
    <div class="tile orange" style="left:60px;top:110px"></div>
    <ul class="contact-list">
      <li><svg viewBox="0 0 24 24"><path d="M6.6 10.8a15.1 15.1 0 0 0 6.6 6.6l2.2-2.2c.3-.3.7-.4 1-.2 1.1.4 2.3.6 3.6.6.6 0 1 .4 1 1V20c0 .6-.4 1-1 1A17 17 0 0 1 3 4c0-.6.4-1 1-1h3.5c.6 0 1 .4 1 1 0 1.3.2 2.5.6 3.6.1.3 0 .7-.2 1z"/></svg>+00 123 456 789</li>
      <li><svg viewBox="0 0 24 24"><path d="M3 5h18v14H3zM4.5 6.5 12 12l7.5-5.5z"/></svg>info@kashvel-led.example</li>
      <li><svg viewBox="0 0 24 24"><circle cx="12" cy="12" r="9"/></svg>www.kashvel-led.example</li>
      <li><svg viewBox="0 0 24 24"><path d="M12 2a7 7 0 0 0-7 7c0 5 7 13 7 13s7-8 7-13a7 7 0 0 0-7-7zm0 9.5A2.5 2.5 0 1 1 12 6.5a2.5 2.5 0 0 1 0 5z"/></svg>Industrial Area, Block 7</li>
    </ul>
    <div class="tile navy" style="left:60px;top:290px"></div>
    <div class="tile navy" style="left:60px;top:364px"></div>
    <div class="tile teal" style="left:134px;top:364px"></div>
    <div class="tile outline-navy" style="left:60px;top:438px"></div>
    <div class="tile teal" style="left:134px;top:438px"></div>
    <div class="tile outline-teal" style="left:208px;top:438px"></div>
  </section>

  <!-- About us -->
  <section class="page about" style="left:170px;top:665px">
    <h2 class="label-box">about us</h2>
    <div class="body-copy" style="position:absolute;left:160px;top:30px;width:210px">
      <p>kashvel LED was founded to serve customers in every lighting need, from engineering and supply to full installation.</p>
    </div>
    <div class="body-copy" style="position:absolute;left:40px;top:150px;width:320px">
      <p style="margin-bottom:14px">Our team designs efficient LED systems for industrial plants, retail shops, gas stations and construction sites.</p>
      <p>We deliver tested products, clear schedules and support long after handover.</p>
    </div>
    <p class="slogan">Lighting for us is not a job<em>it is a Passion</em></p>
    <div class="tile orange" style="left:300px;top:470px;width:60px;height:60px"></div>
  </section>

  <!-- Goals and mission -->
  <section class="page goals" style="left:630px;top:665px">
    <div class="brand"><span class="brand-square"></span>kashvel</div>
    <h2 class="heading" style="top:70px;font-size:28px">Our Goals<br>and Mission</h2>
    <div class="body-copy" style="position:absolute;left:22px;top:150px;width:350px">
      <p style="margin-bottom:10px">Our goal is to bring safe, bright and efficient lighting to every site we serve, while cutting energy use and maintenance for our clients.</p>
      <p>We plan each project with care and deliver on time.</p>
    </div>
    <div role="img" aria-label="Photos of lit industrial plants and retail sites">
      <div class="tile photo-warm" style="left:22px;top:290px;width:110px;height:110px"></div>
      <div class="tile photo" style="left:140px;top:290px;width:110px;height:110px"></div>
      <div class="tile photo-warm" style="left:258px;top:290px;width:110px;height:110px"></div>
      <div class="tile photo" style="left:22px;top:408px;width:110px;height:110px"></div>
    </div>
    <div class="tile teal" style="left:140px;top:408px;width:110px;height:110px"></div>
    <div class="tile orange" style="left:258px;top:408px;width:110px;height:110px"></div>
  </section>

  <!-- Project references -->
  <section class="page references" style="left:170px;top:1280px">
    <h2 class="heading" style="top:40px;font-size:24px;color:var(--navy)">Project<br><span style="color:var(--teal)">References</span></h2>
    <div class="ref-grid" style="top:130px">
      <div class="ref-badge"></div><div class="ref-badge round"></div><div class="ref-badge"></div>
      <div class="ref-badge round"></div><div class="ref-badge"></div><div class="ref-badge"></div>
      <div class="ref-badge"></div><div class="ref-badge"></div><div class="ref-badge round"></div>
      <div class="ref-badge"></div><div class="ref-badge round"></div><div class="ref-badge"></div>
      <div class="ref-badge round"></div><div class="ref-badge"></div><div class="ref-badge"></div>
      <div class="ref-badge"></div><div class="ref-badge"></div><div class="ref-badge round"></div>
      <div class="ref-badge"></div><div class="ref-badge round"></div><div class="ref-badge"></div>
    </div>
  </section>

  <!-- Services -->
  <section class="page services" style="left:630px;top:1280px">
    <h2 class="heading" style="top:50px;left:auto;right:22px;font-size:22px;color:var(--navy)">project cycle</h2>
    <div class="tile orange" style="left:auto;right:180px;top:44px;width:36px;height:36px;border-radius:6px"></div>
    <ul class="service-list">
      <li style="background:var(--navy);width:95%">Site survey</li>
      <li style="background:var(--teal);width:90%">Lighting design</li>
      <li style="background:var(--orange);width:85%">Product approval</li>
      <li style="background:var(--red);width:80%">Supply</li>
      <li style="background:var(--purple);width:75%">Installation</li>
      <li style="background:var(--blue);width:70%">Testing</li>
      <li style="background:var(--green);width:65%">Handover</li>
      <li style="background:#d9a400;width:60%">Maintenance</li>
    </ul>
  </section>

  <!-- Project cycle -->
  <section class="page project-cycle" style="left:400px;top:1895px">
    <h2 class="heading" style="top:40px;font-size:26px;color:var(--navy)">Project cycle</h2>
    <div class="tile orange" style="left:auto;right:22px;top:34px;width:40px;height:40px;border-radius:6px"></div>
    <div class="cycle"><div class="cycle-hub">kashvel<br>LED</div></div>
    <ul class="cycle-labels">
      <li><i style="background:var(--orange)"></i>Site survey</li>
      <li><i style="background:var(--red)"></i>Lighting design</li>
      <li><i style="background:var(--purple)"></i>Product approval</li>
      <li><i style="background:var(--blue)"></i>Supply</li>
      <li><i style="background:var(--teal)"></i>Installation</li>
      <li><i style="background:var(--green)"></i>Testing</li>
      <li><i style="background:var(--navy)"></i>Handover</li>
      <li><i style="background:#f2c94c"></i>Maintenance</li>
    </ul>
  </section>

</main>
</body>
</html>
```